domestic violence campaign

To Whom It May Concern:

We are fully aware that domestic violence can enter anyone’s life at any given time. As women we are faced with many demands as mothers, daughters, wives, sisters, providers, and friends. We often lose ourselves and our confidence. Bright Maple Circle (BMC) Transitional Center of Western New York has embarked on a whole new way of intervention and prevention. As a domestic violence survivor I have created a facility and ideals which will enforce a revolution of Domestic Violence victims. For many years, growing up in suburbs of Western New York, I have come to terms with this fight. Domestic Violence can be stopped and prevented. As a domestic violence victim myself, being in live-in facility, as well as six different domestic violence shelters throughout the state, I fled from my domestic violence abuse. Without those temporary facilities, all that comes to my mind is death. They helped me rebuild and save my life but something was missing – zero education, training programs, parenting classes, personal strengthening workshops, on site at all. Considering the limited amount of time (30-45 days in an average shelter) and lack of resources, I was in need of the tools needed to move me from being a victim to having a stable life.
Opening more doors in Western New York is essential with the surrounding agencies and shelters overwhelmed from assisting women of crisis. Many issues have risen, as a result, such as: over-crowding, long waiting lists, and zero educational training with an on-site teaching curriculum. A repeated vicious cycle – victims regressing and not progressing with over 4000 cases of domestic violence reported throughout Erie County. The opening Bright Maple Circle (BMC) Transitional Center of Western New York will provide a 9-24 month live-in facility, along with educational and training programs on-site that will serve as important tools to domestic violence victims. These educational based facilities and services are well needed for Western New York. Our trained certified staff will provide endless help to domestic violence victim. They will feel safe as they rebuild their lives and take advantage of our educational curriculum that has been designed to increase awareness and provide steppingstones to move the victims into confident stable independent human beings. Our clients will receive complete educational training, state testing, parenting classes, as well as strengthening, coping, and developing skills here at our facility. Bright Maple Circle (BMC) Transitional Center is asking for your support.
Sincerely,
Rosalind Pemberton
President and CEO/website bmctcq.org
Bright Maple Circle (BMC) Transitional Center of WNY

Industry/Entity Type

Training

Requirements
Nice to have
• we have already created our T-shirt/we will like for our T-shirt to be the center of the campaign to T-shirt reads
V IOLENCE
O N
W OMEN
S TOPS the campaign is to raise money so we can open doors and save lives

```html
<!DOCTYPE html>
<html lang="en">
<head>
<meta charset="utf-8">
<title>BMC Front Postcard</title>
<link rel="stylesheet" href="https://fonts.googleapis.com/css2?family=Exo+2:wght@700;800&family=Open+Sans:ital,wght@0,400;0,600;0,700;1,400;1,700&display=swap">
<style>
  :root {
    --stage: #333333;
    --white: #ffffff;
    --purple: #5b2873;
    --purple-deep: #350f45;
    --purple-brand: #6a2a86;
    --ink: #3d3d3d;
    --ink-soft: #555555;
    --gray-light: #e7e7e7;
    --gray-mid: #cdcdcd;
  }
  * { margin: 0; padding: 0; box-sizing: border-box; }
  html, body { width: 1200px; height: 1000px; overflow: hidden; background: var(--stage); }
  .postcard { position: relative; width: 1200px; height: 1000px; font-family: "Open Sans", Arial, sans-serif; }
  .postcard__shapes { position: absolute; inset: 0; }
  .brand { position: absolute; left: 150px; top: 82px; display: flex; align-items: center; gap: 22px; }
  .brand__mark { width: 78px; height: 78px; border-radius: 50%; background: var(--purple-brand); }
  .brand__name { font-family: "Open Sans", Arial, sans-serif; font-weight: 600; font-size: 29px; line-height: 1.08; color: var(--purple-brand); }
  .brand__region { position: absolute; left: 360px; top: 172px; font-size: 20px; color: var(--ink-soft); }
  .donate { position: absolute; left: 690px; top: 70px; width: 390px; text-align: center; color: var(--white); }
  .donate__title { font-family: "Exo 2", Arial, sans-serif; font-weight: 800; font-size: 46px; line-height: 46px; letter-spacing: 1px; }
  .donate__url { font-size: 27px; margin-top: 8px; }
  .message { position: absolute; left: 540px; top: 318px; width: 565px; text-align: center; color: var(--white); }
  .message__strong { font-family: "Exo 2", Arial, sans-serif; font-weight: 800; font-size: 46px; line-height: 52px; letter-spacing: 1.5px; }
  .message__line { font-size: 27px; line-height: 46px; }
  .pledge { position: absolute; left: 555px; top: 645px; width: 480px; text-align: center; color: var(--ink); font-style: italic; }
  .pledge__line { font-size: 26px; line-height: 36px; }
  .pledge__vow { font-size: 33px; font-weight: 700; line-height: 42px; }
  .pledge__phone { font-size: 37px; font-weight: 700; line-height: 44px; }
  .pledge__gap { height: 14px; }
  .vows-tag { position: absolute; left: 212px; top: 535px; width: 262px; height: 318px; transform: rotate(-8deg); border: 5px solid var(--white); border-radius: 24px;
    background: radial-gradient(ellipse at 50% 40%, var(--purple) 0%, var(--purple-deep) 100%); color: var(--white); padding: 40px 0 0 26px; }
  .vows-tag__row { display: block; font-weight: 700; letter-spacing: 3px; font-size: 26px; line-height: 62px; }
  .vows-tag__initial { font-size: 42px; margin-right: 6px; }
  .vows-tag__row--2 { padding-left: 2px; }
  .vows-tag__row--4 { padding-left: 14px; }
</style>
</head>
<body>
<main class="postcard">
  <svg class="postcard__shapes" width="1200" height="1000" viewBox="0 0 1200 1000" aria-hidden="false">
    <defs>
      <clipPath id="card-clip"><rect x="68" y="27" width="1082" height="838"/></clipPath>
      <radialGradient id="band-fill" cx="0.62" cy="0.5" r="0.6">
        <stop offset="0" stop-color="#5e2c76"/>
        <stop offset="1" stop-color="#360f46"/>
      </radialGradient>
      <radialGradient id="oval-fill" cx="0.45" cy="0.4" r="0.65">
        <stop offset="0" stop-color="#5e2c76"/>
        <stop offset="1" stop-color="#360f46"/>
      </radialGradient>
      <linearGradient id="base-fill" x1="0" y1="0" x2="0" y2="1">
        <stop offset="0" stop-color="#e9e9e9"/>
        <stop offset="1" stop-color="#cfcfcf"/>
      </linearGradient>
      <linearGradient id="photo-fill" x1="0" y1="0" x2="1" y2="0">
        <stop offset="0" stop-color="#8d8d8d"/>
        <stop offset="0.35" stop-color="#d4d4d4"/>
        <stop offset="0.7" stop-color="#f2f2f2"/>
        <stop offset="1" stop-color="#f2f2f2" stop-opacity="0"/>
      </linearGradient>
    </defs>
    <g clip-path="url(#card-clip)">
      <rect class="card" x="68" y="27" width="1082" height="838" fill="#ffffff"/>
      <path class="band" d="M68,268 C300,232 600,236 800,258 C960,276 1080,272 1150,252 L1150,615 L68,615 Z" fill="url(#band-fill)"/>
      <path class="band-edge" d="M68,262 C300,226 600,230 800,252 C960,270 1080,266 1150,246" fill="none" stroke="#e2e2e2" stroke-width="4"/>
      <g role="img" aria-label="Black and white photo of a frightened woman shielding her head from a raised fist">
        <path d="M68,262 C250,236 420,232 560,236 L560,615 L68,615 Z" fill="url(#photo-fill)"/>
      </g>
      <rect class="base" x="68" y="615" width="1082" height="250" fill="url(#base-fill)"/>
      <line x1="68" y1="616" x2="1150" y2="616" stroke="#ffffff" stroke-width="4"/>
      <ellipse class="donate-oval" cx="885" cy="132" rx="192" ry="124" fill="url(#oval-fill)" stroke="#ffffff" stroke-width="5"/>
    </g>
  </svg>

  <div class="brand">
    <span class="brand__mark"></span>
    <span class="brand__name">Bright Maple Circle<br>Transitional Center</span>
  </div>
  <div class="brand__region">Western New York</div>

  <div class="donate">
    <div class="donate__title">DONATE<br>TODAY</div>
    <div class="donate__url">www.bmctcq.org</div>
  </div>

  <div class="message">
    <div class="message__strong">DOMESTIC VIOLENCE</div>
    <div class="message__line">can enter anyone’s life at any given</div>
    <div class="message__strong">TIME</div>
    <div class="message__line">Domestic Violence can be stopped or</div>
    <div class="message__strong">PREVENTED</div>
  </div>

  <div class="pledge">
    <div class="pledge__line">Place your Ad, and speak out take the</div>
    <div class="pledge__vow">“Vows with BMC”</div>
    <div class="pledge__gap"></div>
    <div class="pledge__line">Call Today for More Information</div>
    <div class="pledge__phone">(716) 555-0142</div>
  </div>

  <div class="vows-tag">
    <span class="vows-tag__row vows-tag__row--1"><span class="vows-tag__initial">V</span>iolence</span>
    <span class="vows-tag__row vows-tag__row--2"><span class="vows-tag__initial">O</span>n</span>
    <span class="vows-tag__row vows-tag__row--3"><span class="vows-tag__initial">W</span>omen</span>
    <span class="vows-tag__row vows-tag__row--4"><span class="vows-tag__initial">S</span>tops</span>
  </div>
</main>
</body>
</html>
```